Basis-Buchdesign für eine Buchserie
Zielgruppe
Privatperson. Ich möchte Bücher zu Themen schreiben, die uns alle bewegen, wo aber alles schiefläuft.
Aufgabenstellung
Buchserie
Mein Kopf ist voller Gedanken, ich will all das nun niederschreiben. Ich habe bereits ein Buch geschrieben. Da ich aber dabei anonym sein musste, konnte ich keine Werbung schalten, nur sehr wenige Exemplare wurden verkauft.
Mir geht es aber gar nicht ums Geld. Ich will einfach das niederschreiben, was gesagt werden muss. Aber diesmal unter meinem echten Namen. Es sind mehrere Oberthemen, die mich interessieren. Für jedes dieser Themen möchte ich ein eigenes Buch schreiben.
Da es mehrere Bücher sein sollen, muss das „Basisdesign“ für alle Bücher gleich sein. Jedes einzelne Thema wird dann zusätzlich mit eigenen Schwerpunkten hervorgehoben, ein Überlagern, ein Ergänzen usw. des Basisdesigns findet statt.
Das Fundament fürs Basisdesign sind meine Grundgedanken, welche die heutige Zeit beschreiben: Frustration, Ohnmacht, Hoffnungslosigkeit, Untergangsszenario, …
Es geht darum, dass derzeit alles auf der Welt nicht normal verläuft. Kaum ein Land wird von einem normalen Demokraten geführt, überall gewinnen ausschließlich Nazis und Vollidioten. Im Kern der Gesellschaft gibt es keinen Zusammenhalt mehr, die durchschnittliche Intelligenz sinkt, Dumme und Idioten haben Hochkonjunktur.
Die Themen, die ich aus heutiger Sicht angehen will, sind:
- Justiz/Polizei/Gesellschaft im Umgang mit Tätern
- Politik (Österreich und allgemein), Schwerpunkt Lügner und Hetzer
- Genderwahnsinn
- Individualverkehr (in Wien)
- Schulsystem (ich bin Lehrer, „gefangen“ in einem maroden System)
Das konkrete Thema für jetzt:
Österreich ist ein Paradis für Täter. Täter werden mit Samthandschuhen angefasst. Fast niemand wird bei einer ersten kriminellen Handlung wirklich bestraft, das Zauberwort heißt „Bewährung“. Jedem Täter gibt man 10-20 Chancen.
Menschen, die sich wehren, werden definitiv bestraft und das auch noch mit höheren Strafen, „Notwehrüberschreitung“ nennen sie das. In vielen Fällen..

```html
<!DOCTYPE html>
<html lang="de">
<head>
<meta charset="utf-8">
<title>Das Opfer – Maxx Mustermann</title>
<link rel="stylesheet" href="https://fonts.googleapis.com/css2?family=EB+Garamond:wght@500&family=Roboto:wght@400&display=swap">
<style>
  :root {
    --cover-black: #0a0507;
    --signal-red: #f0452a;
    --halftone-orange: #f24a25;
    --paper-white: #ffffff;
  }
  html, body {
    margin: 0;
    padding: 0;
    overflow: hidden;
    background: var(--cover-black);
  }
  .book-cover {
    position: relative;
    width: 846px;
    height: 1200px;
    overflow: hidden;
    background: var(--cover-black);
  }
  .cover-artwork {
    position: absolute;
    inset: 0;
    background:
      radial-gradient(ellipse 110px 200px at 730px 500px, rgba(242,74,37,0.55), rgba(242,74,37,0) 100%),
      radial-gradient(ellipse 330px 520px at 150px 560px, rgba(242,74,37,0.85) 0%, rgba(242,74,37,0.6) 55%, rgba(242,74,37,0) 100%),
      radial-gradient(ellipse 220px 260px at 300px 1080px, rgba(242,74,37,0.75), rgba(242,74,37,0) 100%);
  }
  .author-name {
    position: absolute;
    top: 96px;
    right: 49px;
    margin: 0;
    font-family: "Roboto", sans-serif;
    font-weight: 400;
    font-size: 27px;
    line-height: 1;
    color: var(--paper-white);
  }
  .book-title {
    margin: 0;
    font-family: "EB Garamond", serif;
    font-weight: 500;
    line-height: 1;
  }
  .book-title__line {
    position: absolute;
    display: block;
  }
  .book-title__line--article {
    top: 727px;
    right: 72px;
    font-size: 129px;
    color: var(--signal-red);
  }
  .book-title__line--noun {
    top: 832px;
    right: 54px;
    font-size: 145px;
    color: var(--paper-white);
    letter-spacing: -2px;
  }
</style>
</head>
<body>
  <main class="book-cover">
    <div class="cover-artwork" role="img" aria-label="Orangefarbenes Rasterpunkt-Porträt eines Kopfes im Profil auf schwarzem Grund"></div>
    <p class="author-name">Maxx Mustermann</p>
    <h1 class="book-title">
      <span class="book-title__line book-title__line--article">DAS</span>
      <span class="book-title__line book-title__line--noun">OPFER</span>
    </h1>
  </main>
</body>
</html>
```